Advertising poster for podcast event

"The Lantern Table" is one of the most popular podcasts in Switzerland (https://listen.brovakast.example/show/4kqPLmWX317TRvbnQ8ZsHD). It is hosted by the two radio DJs Lukas Brandt and Adrian Furrer. For a series of live shows where the podcast is recorded with an audience, we need a design of a poster. This should have the format A3 high. In addition, the image must be used that was uploaded here, because this is the cover photo with which you can always recognize the podcast. But what is designed around it is up to you. In addition, it must contain the following text:

- Title of the event:
The lantern table - Live
- Show dates:
Saturday, November 11, 2023 - Solothurn
Wednesday, December 27, 2023 - Berne
Thursday, December 28, 2023 - Berne
- A line with additional information about the presale:
The pavilion, information and tickets: www.diekuppel.example

Target Market(s)

Switzerland

Industry/Entity Type

Entertainment

Requirements
Must have
• The attached image and text according to the briefing.

```html
<!DOCTYPE html>
<html lang="en">
<head>
<meta charset="utf-8">
<title>The Lantern Table – Live</title>
<link rel="stylesheet" href="https://fonts.googleapis.com/css2?family=Bebas+Neue&family=Oswald:wght@500;700&display=swap">
<style>
  :root {
    --frame: #000000;
    --orange: #f7a81c;
    --white: #ffffff;
    --rule: #f2e48a;
    --sign-fill: #3a2915;
    --sign-edge: #1f150b;
    --live-red: #d51f26;
    --bottom-top: #4d3c20;
    --bottom-end: #3a2a1b;
  }
  * { margin: 0; padding: 0; box-sizing: border-box; }
  html, body { width: 904px; height: 1200px; overflow: hidden; background: var(--frame); }
  .canvas { position: relative; width: 904px; height: 1200px; background: var(--frame); }
  .poster {
    position: absolute; left: 92px; top: 89px; width: 720px; height: 1021px; overflow: hidden;
    background: linear-gradient(180deg, var(--bottom-top) 0%, var(--bottom-end) 100%);
    font-family: "Bebas Neue", "Oswald", sans-serif;
  }
  .cover-photo {
    position: absolute; left: 0; top: 0; width: 720px; height: 560px;
    background:
      radial-gradient(ellipse 240px 260px at 30% 75%, rgba(80,50,60,0.55), transparent 70%),
      linear-gradient(90deg, #d6482a 0%, #a63a2c 30%, #3d2d3a 65%, #352838 100%);
    -webkit-mask-image: linear-gradient(180deg, #000 82%, transparent 100%);
            mask-image: linear-gradient(180deg, #000 82%, transparent 100%);
  }
  .hosts-illustration {
    position: absolute; left: 98px; top: 85px; width: 516px; height: 400px;
    background: linear-gradient(90deg, #241d1d 0%, #2a2222 50%, #a9b6d8 62%, #b7a3b6 100%);
    opacity: 0.85;
    border-radius: 90px 90px 0 0;
  }
  .sign { position: absolute; left: 0; top: 0; width: 720px; height: 1021px; }
  .live-badge {
    position: absolute; left: 317px; top: 432px; width: 85px; height: 28px;
    background: var(--live-red); border-radius: 14px;
    color: var(--white); font-family: "Oswald", sans-serif; font-weight: 700;
    font-size: 20px; line-height: 28px; text-align: center; letter-spacing: 1px;
  }
  .event-title {
    position: absolute; left: 0; width: 720px; text-align: center; font-weight: 400;
    color: var(--white); font-size: 112px; line-height: 1; top: 478px; letter-spacing: 1px;
  }
  .event-subtitle {
    position: absolute; left: 0; width: 720px; text-align: center; top: 584px;
    color: var(--orange); font-size: 54px; line-height: 1; letter-spacing: 4px;
  }
  .hosts {
    position: absolute; left: 0; width: 720px; top: 745px; text-align: center;
    color: var(--orange); font-size: 46px; line-height: 1;
  }
  .rule { position: absolute; left: 54px; width: 610px; height: 1px;
    background: linear-gradient(90deg, transparent, var(--rule) 8%, var(--rule) 92%, transparent); }
  .rule--top { top: 803px; }
  .rule--bottom { top: 915px; }
  .dates { position: absolute; left: 54px; top: 814px; width: 610px; height: 82px; display: flex; }
  .show { flex: 1; text-align: center; font-size: 25px; line-height: 27px; }
  .show + .show { border-left: 1.5px solid var(--rule); }
  .show__day, .show__city { color: var(--white); }
  .show__date { color: var(--orange); }
  .presale {
    position: absolute; left: 0; width: 720px; top: 934px; text-align: center;
    color: var(--white); font-size: 31px; line-height: 1; white-space: nowrap;
  }
  .presale__link { color: var(--orange); margin-left: 10px; }
</style>
</head>
<body>
<div class="canvas">
  <main class="poster">
    <div class="cover-photo" role="img" aria-label="Podcast cover photo: studio microphone in red and violet light"></div>
    <div class="hosts-illustration" role="img" aria-label="Illustrated portraits of the two podcast hosts"></div>

    <svg class="sign" viewBox="0 0 720 1021" aria-hidden="true">
      <polygon points="361,371 640,455 640,605 361,688 79,605 79,455"
               fill="none" stroke="var(--rule)" stroke-width="4" stroke-linejoin="round"/>
      <polygon points="361,388 622,466 622,595 361,672 97,595 97,466"
               fill="var(--sign-fill)" stroke="var(--sign-edge)" stroke-width="4" stroke-linejoin="round"/>
    </svg>

    <div class="live-badge">LIVE</div>
    <h1 class="event-title">THE LANTERN</h1>
    <div class="event-subtitle">TABLE</div>

    <p class="hosts">DJ LUKAS BRANDT &amp; DJ ADRIAN FURRER</p>
    <div class="rule rule--top"></div>
    <section class="dates">
      <div class="show">
        <div class="show__day">SATURDAY</div>
        <div class="show__date">NOVEMBER 11, 2023</div>
        <div class="show__city">SOLOTHURN</div>
      </div>
      <div class="show">
        <div class="show__day">WEDNESDAY</div>
        <div class="show__date">DECEMBER 27, 2023</div>
        <div class="show__city">BERNE</div>
      </div>
      <div class="show">
        <div class="show__day">THURSDAY</div>
        <div class="show__date">DECEMBER 28, 2023</div>
        <div class="show__city">BERNE</div>
      </div>
    </section>
    <div class="rule rule--bottom"></div>
    <p class="presale">THE PAVILION, INFORMATION AND TICKETS:<span class="presale__link">WWW.DIEKUPPEL.EXAMPLE</span></p>
  </main>
</div>
</body>
</html>
```